Rimo Application for Cars Accidents Services

We need app screen designs for company provide services for the cars that got accidents, the design should be modern official and simple, the pages around 26 include login, register, auth code, home, splash, request service, profile, settings, booking, booking info ..., we need something so professional please.

Target Market(s)

Cars owners

```html
<!DOCTYPE html>
<html lang="en">
<head>
<meta charset="utf-8">
<title>Rimo – App Screens</title>
<link rel="stylesheet" href="https://fonts.googleapis.com/css2?family=Montserrat:wght@700;800&family=Open+Sans:wght@300;400;600;700&display=swap">
<style>
:root{
  --stage:#e3e3e7;
  --green:#3a9a0e;
  --sky:#c4eefa;
  --mist:#e1eff1;
  --field:#eefbff;
  --ink:#141414;
  --muted:#3a3a3a;
  --line:#dcdcdc;
  --road-top:#6fc2dc;
  --road-bottom:#2f8aa6;
}
*{margin:0;padding:0;box-sizing:border-box}
html,body{width:1200px;height:449px;overflow:hidden;background:var(--stage)}
body{position:relative;font-family:"Open Sans",sans-serif;color:var(--ink)}
.screen{position:absolute;overflow:hidden}
.screen--compact{left:48px;top:45px;width:177px;height:354px;border-radius:14px;background:var(--sky)}
.screen--login{left:269px;top:35px;width:209px;height:372px;background:var(--sky)}
.screen--tour{left:496px;top:35px;width:209px;height:372px;background:var(--mist)}
.screen--profile{left:722px;top:35px;width:209px;height:372px;background:#fff}
.screen--car{left:951px;top:35px;width:209px;height:372px;background:#fff}
.abs{position:absolute}
.brand{position:absolute;left:0;right:0;display:flex;align-items:center;justify-content:center;gap:5px;
  font-family:"Montserrat",sans-serif;font-weight:800;color:var(--ink);letter-spacing:1px}
.brand__dot{width:10px;height:10px;border-radius:50%;background:var(--ink)}
.title{position:absolute;left:0;right:0;text-align:center;font-family:"Montserrat",sans-serif;font-weight:800;color:var(--ink)}
.tagline{position:absolute;left:0;right:0;text-align:center;font-weight:400;color:var(--ink)}
.field{position:absolute;background:var(--field);font-size:6.5px;font-weight:600;color:var(--muted);display:flex;align-items:center;padding-left:11px}
.btn{position:absolute;background:var(--green);color:#fff;font-family:"Montserrat",sans-serif;font-weight:800;display:flex;align-items:center;justify-content:center;gap:9px}
.signup{position:absolute;display:flex;justify-content:space-between;font-size:6.5px;color:var(--ink)}
.signup b{font-weight:700}
.scene{position:absolute;left:0;right:0;bottom:0}
.scene--highway{background:linear-gradient(180deg,var(--sky) 0%,#8fd0e4 30%,var(--road-top) 45%,var(--road-bottom) 100%)}
.scene--city{background:linear-gradient(180deg,var(--mist) 0%,#bfe2ec 35%,#7fb7c9 65%,#8a8f96 80%,#7a7f86 100%)}
.topbar{position:absolute;left:0;top:0;right:0;height:28px;background:var(--green);color:#fff;display:flex;align-items:center;padding:0 8px;gap:6px;
  font-family:"Montserrat",sans-serif;font-weight:800;font-size:8px}
.topbar__tools{margin-left:auto;display:flex;gap:9px}
.menu{position:absolute;left:12px;width:185px;top:122px;list-style:none}
.menu__item{height:38px;border-bottom:1.5px solid var(--line);display:flex;align-items:center;gap:6px;font-size:9px;padding:0 2px}
.menu__item span{flex:1}
.car-photo{position:absolute;left:0;right:0;top:62px;height:108px;background:radial-gradient(ellipse at 55% 55%,#f4f4f4 0%,#d9d9d9 40%,#fff 75%)}
.car-name{position:absolute;left:0;right:0;top:183px;text-align:center;font-family:"Montserrat",sans-serif;font-weight:800;font-size:12px}
.car-trim{position:absolute;left:0;right:0;top:205px;text-align:center;font-size:8px;font-weight:400}
.car-price{position:absolute;left:0;right:0;top:227px;text-align:center;font-size:19px;font-weight:300}
.car-price small{font-size:8px;font-weight:400}
.chip{position:absolute;top:273px;height:23px;width:61px;border:1.5px solid #9a9a9a;border-radius:2px;display:flex;align-items:center;justify-content:center;gap:5px;font-size:7.5px}
.heart{position:absolute;left:182px;top:44px}
</style>
</head>
<body>

<!-- Login, compact -->
<section class="screen screen--compact">
  <div class="brand" style="top:33px;font-size:18px"><i class="brand__dot"></i>RIMO</div>
  <div class="title" style="top:87px;font-size:11.5px">CAR RENTAL</div>
  <div class="tagline" style="top:102px;font-size:9.5px">Travel, Love a Car</div>
  <div class="field" style="left:6px;top:131px;width:167px;height:27px">Email Address</div>
  <div class="field" style="left:6px;top:165px;width:167px;height:27px">Password</div>
  <div class="btn" style="left:6px;top:199px;width:167px;height:27px;font-size:10.5px">LOGIN ME</div>
  <div class="signup" style="left:5px;right:3px;top:236px"><span>Don't have a account?</span><b>Membership</b></div>
  <div class="scene scene--highway" style="top:247px" role="img" aria-label="Illustration of cars driving on a highway toward a city skyline"></div>
</section>

<!-- Login -->
<section class="screen screen--login">
  <div class="brand" style="top:28px;font-size:20px"><i class="brand__dot"></i>RIMO</div>
  <div class="title" style="top:84px;font-size:12.5px">CAR RENTAL</div>
  <div class="tagline" style="top:100px;font-size:10.5px">Travel, Love a Car</div>
  <div class="field" style="left:14px;top:132px;width:181px;height:29px">Email Address</div>
  <div class="field" style="left:14px;top:168px;width:181px;height:29px">Password</div>
  <div class="btn" style="left:14px;top:205px;width:181px;height:29px;font-size:11.5px">LOGIN ME</div>
  <div class="signup" style="left:14px;right:14px;top:245px"><span>Don't have a account?</span><b>Membership</b></div>
  <div class="scene scene--highway" style="top:259px" role="img" aria-label="Illustration of cars driving on a highway toward a city skyline"></div>
</section>

<!-- Tour -->
<section class="screen screen--tour">
  <div class="brand" style="top:36px;font-size:20px"><i class="brand__dot"></i>RIMO</div>
  <div class="title" style="top:99px;font-size:12.5px;line-height:17px">TAKE TOUR<br>TO OUR SERVICES</div>
  <div class="btn" style="left:30px;top:157px;width:150px;height:33px;font-size:11px">
    <svg width="14" height="14" viewBox="0 0 24 24" fill="#fff"><path d="M12 8a4 4 0 100 8 4 4 0 000-8zm9.4 5.3l-2-.3a7.6 7.6 0 01-.7 1.7l1.2 1.6-1.9 1.9-1.6-1.2a7.6 7.6 0 01-1.7.7l-.3 2h-2.8l-.3-2a7.6 7.6 0 01-1.7-.7l-1.6 1.2-1.9-1.9 1.2-1.6a7.6 7.6 0 01-.7-1.7l-2-.3v-2.8l2-.3a7.6 7.6 0 01.7-1.7L4.6 6.8l1.9-1.9 1.6 1.2a7.6 7.6 0 011.7-.7l.3-2h2.8l.3 2a7.6 7.6 0 011.7.7l1.6-1.2 1.9 1.9-1.2 1.6a7.6 7.6 0 01.7 1.7l2 .3z"/></svg>
    ASK SERVICE</div>
  <div class="btn" style="left:30px;top:203px;width:150px;height:33px;font-size:11px">
    <svg width="16" height="13" viewBox="0 0 24 20" fill="#fff"><path d="M5 2h14l3 7v9h-3v-2H5v2H2V9zm1.5 2L4.5 8h15l-2-4zM6 11a1.5 1.5 0 100 3 1.5 1.5 0 000-3zm12 0a1.5 1.5 0 100 3 1.5 1.5 0 000-3z"/></svg>
    CAR RENTAL</div>
  <div class="scene scene--city" style="top:268px" role="img" aria-label="Illustration of a city street with cars and buildings"></div>
</section>

<!-- Profile menu -->
<section class="screen screen--profile">
  <header class="topbar">
    <svg width="7" height="10" viewBox="0 0 7 10"><path d="M6 1L2 5l4 4" stroke="#fff" stroke-width="1.6" fill="none"/></svg>
    MY PROFILE
  </header>
  <div class="brand" style="top:62px;font-size:22px"><i class="brand__dot"></i>RIMO</div>
  <ul class="menu">
    <li class="menu__item"><svg width="10" height="10" viewBox="0 0 10 10"><circle cx="5" cy="3" r="2.3"/><path d="M.8 10a4.2 4 0 018.4 0z"/></svg><span>My Profile</span><svg width="6" height="9"><path d="M1 1l3.5 3.5L1 8" stroke="#222" stroke-width="1.3" fill="none"/></svg></li>
    <li class="menu__item"><svg width="10" height="10" viewBox="0 0 10 10"><circle cx="5" cy="5" r="4"/></svg><span>About Rimo</span><svg width="6" height="9"><path d="M1 1l3.5 3.5L1 8" stroke="#222" stroke-width="1.3" fill="none"/></svg></li>
    <li class="menu__item"><svg width="11" height="11" viewBox="0 0 11 11"><circle cx="5.5" cy="5.5" r="4.6" fill="none" stroke="#222"/><text x="5.5" y="8" font-size="7" text-anchor="middle" font-family="Open Sans">?</text></svg><span>General Questions</span><svg width="6" height="9"><path d="M1 1l3.5 3.5L1 8" stroke="#222" stroke-width="1.3" fill="none"/></svg></li>
    <li class="menu__item"><svg width="10" height="10" viewBox="0 0 10 10"><circle cx="5" cy="5" r="3.2" fill="none" stroke="#222" stroke-width="2.2" stroke-dasharray="1.6 1"/><circle cx="5" cy="5" r="1.2"/></svg><span>Settings</span><svg width="6" height="9"><path d="M1 1l3.5 3.5L1 8" stroke="#222" stroke-width="1.3" fill="none"/></svg></li>
    <li class="menu__item" style="height:43px"><svg width="11" height="10" viewBox="0 0 11 10"><path d="M4 .5l6 4.5-4 4.5L0 5z"/></svg><span>My Tickets</span><svg width="6" height="9"><path d="M1 1l3.5 3.5L1 8" stroke="#222" stroke-width="1.3" fill="none"/></svg></li>
  </ul>
</section>

<!-- Car detail -->
<section class="screen screen--car">
  <header class="topbar">
    <svg width="7" height="10" viewBox="0 0 7 10"><path d="M6 1L2 5l4 4" stroke="#fff" stroke-width="1.6" fill="none"/></svg>
    SPORTS CAR
    <span class="topbar__tools">
      <svg width="10" height="10" viewBox="0 0 10 10"><circle cx="4" cy="4" r="3" stroke="#fff" stroke-width="1.4" fill="none"/><path d="M6.3 6.3L9.3 9.3" stroke="#fff" stroke-width="1.5"/></svg>
      <svg width="12" height="11" viewBox="0 0 12 11" stroke="#fff" fill="none"><path d="M0 2h12M0 5.5h12M0 9h12"/><circle cx="8" cy="2" r="1.3" fill="var(--green)"/><circle cx="4" cy="5.5" r="1.3" fill="var(--green)"/><circle cx="8" cy="9" r="1.3" fill="var(--green)"/></svg>
    </span>
  </header>
  <svg class="heart" width="14" height="13" viewBox="0 0 14 13"><path d="M7 12L1.6 6.6A3.2 3.2 0 017 2.2a3.2 3.2 0 015.4 4.4z" fill="none" stroke="#222" stroke-width="1.1"/></svg>
  <div class="car-photo" role="img" aria-label="Photo of a white sports coupe"></div>
  <div class="car-name">VEXA CORSAIR</div>
  <div class="car-trim">TURBO LINE</div>
  <div class="car-price">240SR <small>/ DAY</small></div>
  <div class="chip" style="left:35px"><svg width="14" height="9" viewBox="0 0 14 9" fill="#333"><rect x="2" y="2" width="9" height="6" rx="1"/><rect x="0" y="4" width="2" height="2"/><rect x="11" y="3" width="3" height="4"/><rect x="4" y="0" width="4" height="2"/></svg>FULL</div>
  <div class="chip" style="left:103px"><svg width="9" height="11" viewBox="0 0 9 11" fill="#333"><rect x="2" y="0" width="5" height="7" rx="1"/><rect x="0" y="7" width="9" height="3"/></svg>5 SEATS</div>
  <div class="btn" style="left:67px;top:319px;width:75px;height:29px;font-size:11.5px">BOOK</div>
</section>

</body>
</html>
```